VR Business Card

Design new business cards for VELMOsoft

Please see attached for the design brief

**** Please note, please feel free to propose a font that works for a professional, technology company ***

Target Market(s)

Technology buyers

Industry/Entity Type

Business

```html
<!DOCTYPE html>
<html lang="en">
<head>
<meta charset="utf-8">
<title>Velmosoft Business Card</title>
<link rel="stylesheet" href="https://fonts.googleapis.com/css2?family=Arimo:wght@400&family=IBM+Plex+Mono:wght@300&family=Roboto+Condensed:wght@400&display=swap">
<style>
  :root {
    --paper: #ffffff;
    --forest: #0b6338;
    --amber: #f39a1e;
    --ink-navy: #2a2468;
  }
  html, body {
    margin: 0;
    padding: 0;
    width: 1200px;
    height: 791px;
    overflow: hidden;
    background: var(--paper);
  }
  .card {
    position: relative;
    width: 1200px;
    height: 791px;
    background: var(--paper);
    font-family: "Arimo", Arial, sans-serif;
  }
  .brand-name {
    position: absolute;
    left: 72px;
    top: 92px;
    margin: 0;
    font-family: "Arimo", Arial, sans-serif;
    font-weight: 400;
    font-size: 46px;
    line-height: 1;
    color: var(--ink-navy);
  }
  .tagline {
    position: absolute;
    left: 448px;
    top: 90px;
    margin: 0;
    font-family: "IBM Plex Mono", "Courier New", monospace;
    font-weight: 300;
    font-size: 34px;
    letter-spacing: 2px;
    line-height: 1.2;
    color: var(--ink-navy);
  }
  .panels {
    position: absolute;
    left: 0;
    top: 0;
  }
  .holder {
    position: absolute;
    left: 102px;
    width: 402px;
    top: 484px;
    text-align: center;
    font-size: 38px;
    color: var(--amber);
    line-height: 1;
  }
  .holder-rule {
    position: absolute;
    left: 102px;
    top: 529px;
    width: 402px;
    height: 6px;
    border-radius: 3px;
    background: var(--amber);
  }
  .contacts {
    position: absolute;
    left: 661px;
    top: 466px;
    margin: 0;
    color: var(--amber);
  }
  .contact-row {
    display: flex;
    align-items: baseline;
    height: 52px;
  }
  .contact-label {
    width: 144px;
    font-size: 37px;
  }
  .contact-value {
    margin: 0;
    font-size: 35px;
    letter-spacing: 1px;
  }
  .contact-value.email {
    font-family: "Roboto Condensed", "Arial Narrow", sans-serif;
    font-size: 32px;
    letter-spacing: -0.5px;
  }
</style>
</head>
<body>
<div class="card">
  <p class="brand-name">Velmosoft</p>
  <p class="tagline">building what comes next....</p>

  <svg class="panels" width="1200" height="791" viewBox="0 0 1200 791" aria-hidden="true">
    <path fill="var(--forest)" d="M0 488 Q0 441 48 441 L558 441 Q596 441 606 472 Q614 441 652 441 L1152 441 Q1200 441 1200 488 L1200 791 L0 791 Z"/>
  </svg>

  <div class="holder">Daniel Moser CEO</div>
  <div class="holder-rule"></div>

  <dl class="contacts">
    <div class="contact-row"><dt class="contact-label">Phone:</dt><dd class="contact-value">+41 41 555 0120</dd></div>
    <div class="contact-row"><dt class="contact-label">Direct:</dt><dd class="contact-value">+41 41 555 0121</dd></div>
    <div class="contact-row"><dt class="contact-label">Fax:</dt><dd class="contact-value">+41 800 555 019</dd></div>
    <div class="contact-row"><dt class="contact-label">Mobile:</dt><dd class="contact-value">+41 78 5550198</dd></div>
    <div class="contact-row"><dt class="contact-label">Email:</dt><dd class="contact-value email">d.moser@velmosoft-it.com</dd></div>
  </dl>
</div>
</body>
</html>
```